Building company buisness cards

We are looking for a sharp modern new look for our business cards.We are a New Zealand based company that specialises in house and land packages.We have attached a photo of the current logo and would like to see if it can be improved somehow if needed.We are open to any colours but we have chosen Black and White at this stage. Feel free to change the font and make the logo smarter looking.Play with the colours and see what looks best.We want a card that looks so good know one will want to throw it away!

Target Market(s)

Building profesonals, home buyers

Industry/Entity Type

Building

Contact Information for Business Card

Derek Haskins
0274930268
derekh@stonerange.co.nz

Font styles to use
Serif
Sans Serif

Colors

Designer to choose colors to be used in the design.

Requirements
Must have
• Just the logo on one side and details on the other
• Clean simple looking card
Nice to have
• Round corners and detail like raised or spot UV
• Something that stands out
Should not have
• To title needed, Director etc

```html
<!DOCTYPE html>
<html lang="en">
<head>
<meta charset="utf-8">
<title>Stone Range business cards</title>
<link href="https://fonts.googleapis.com/css2?family=Montserrat:wght@400;500;600&display=swap" rel="stylesheet">
<style>
  :root {
    --backdrop: #2b2623;
    --card: #1e1e1f;
    --card-edge: #d8322a;
    --emboss: #2c2c2e;
    --emboss-light: #3a3a3d;
    --ink-light: #f2f2f2;
    --ink-muted: #cfcfcf;
    --panel: #ffffff;
    --ink-dark: #1a1a1a;
  }
  * { margin: 0; padding: 0; box-sizing: border-box; }
  html, body {
    width: 1200px; height: 1055px; overflow: hidden;
    background: var(--backdrop);
    font-family: "Montserrat", sans-serif;
  }
  .canvas { position: relative; width: 1200px; height: 1055px; }

  .logo-panel {
    position: absolute; left: 696px; top: 0;
    width: 504px; height: 222px;
    background: var(--panel);
    display: flex; align-items: center; justify-content: center;
  }
  .logo-panel .brand-name {
    font-size: 60px; font-weight: 500; color: var(--ink-dark);
  }

  .card {
    position: absolute;
    width: 500px; height: 290px;
    background: var(--card);
    border-radius: 26px;
    border-bottom: 5px solid var(--card-edge);
    border-right: 3px solid var(--card-edge);
  }
  .card-front { left: 70px; top: 330px; display: flex; align-items: center; justify-content: center; }
  .card-back { left: 630px; top: 500px; display: flex; align-items: center; padding: 0 34px; }

  .brand-mark { display: flex; align-items: center; gap: 14px; }
  .brand-mark .dot {
    width: 16px; height: 16px; background: var(--emboss-light);
  }
  .brand-mark .brand-name {
    font-size: 40px; font-weight: 500; color: var(--emboss-light);
  }
  .card-back .brand-name { font-size: 28px; }

  .divider {
    width: 1px; height: 120px; background: var(--ink-muted);
    margin: 0 22px; opacity: .7;
  }
  .details { color: var(--ink-light); }
  .details .person {
    font-size: 18px; font-weight: 600; letter-spacing: 1px;
    text-transform: uppercase; margin-bottom: 16px;
  }
  .details .line {
    display: flex; align-items: center; gap: 9px;
    font-size: 13px; color: var(--ink-muted); margin-bottom: 7px;
  }
  .details svg { width: 12px; height: 12px; flex: none; }
</style>
</head>
<body>
<main class="canvas">
  <section class="logo-panel">
    <span class="brand-name">Stone Range</span>
  </section>

  <article class="card card-front">
    <div class="brand-mark">
      <span class="dot"></span>
      <span class="brand-name">Stone Range</span>
    </div>
  </article>

  <article class="card card-back">
    <div class="brand-mark">
      <span class="dot"></span>
      <span class="brand-name">Stone Range</span>
    </div>
    <span class="divider"></span>
    <div class="details">
      <p class="person">Derek Haskins</p>
      <p class="line">
        <svg viewBox="0 0 24 24" fill="currentColor"><path d="M6.6 10.8a15 15 0 0 0 6.6 6.6l2.2-2.2c.3-.3.7-.4 1-.2 1.1.4 2.3.6 3.6.6.6 0 1 .4 1 1V20c0 .6-.4 1-1 1A17 17 0 0 1 3 4c0-.6.4-1 1-1h3.5c.6 0 1 .4 1 1 0 1.3.2 2.5.6 3.6.1.3 0 .7-.2 1z"/></svg>
        0274930268
      </p>
      <p class="line">
        <svg viewBox="0 0 24 24" fill="none" stroke="currentColor" stroke-width="2"><rect x="3" y="5" width="18" height="14"/><path d="M3 5l9 8 9-8"/></svg>
        derekh@stonerange.co.nz
      </p>
      <p class="line">
        <svg viewBox="0 0 24 24" fill="none" stroke="currentColor" stroke-width="2"><circle cx="12" cy="12" r="9"/><path d="M3 12h18M12 3c3 3 3 15 0 18M12 3c-3 3-3 15 0 18"/></svg>
        www.stonerange.co.nz
      </p>
    </div>
  </article>
</main>
</body>
</html>
```